Wholesale Company Needs a Flyer

We are a general product wholesale company based in Puerto Rico. We need a flyer to hand out at an upcoming gas station association convention. Our logo should be integrated into the design. We want something catchy and memorable. Feel free to play around with colors. You can visit our website, www.morvellanwares.com, so you can understand our business better. Also attached a sample of a flyer made once before.
Updates

Industry/Entity Type

Gas Station

Font styles to use
Serif

Requirements
Must have
• The flyer must have the companies information:
• Address- Calle Ledanto #42
• Rpto Ind Ledanto
• Bayamón, PR 00958
• Telf. 787-614-3927 / 787-652-7193
• Email. info@morvellanwares.com
• website. www.morvellanwares.com
• Integrate our logo into the design.
Nice to have
• We would like an eye catching design that stands out. Somehow integrating the gas station theme into it if possible.

```html
<!DOCTYPE html>
<html lang="en">
<head>
<meta charset="utf-8">
<title>Morvellan Wares, Inc. — Flyer</title>
<link href="https://fonts.googleapis.com/css2?family=Jost:wght@300;400;500&display=swap" rel="stylesheet">
<style>
  :root {
    --brand-green: #22b33a;
    --brand-red: #e0262b;
    --paper: #ffffff;
    --ink: #333333;
    --ink-light: #ffffff;
    --panel: rgba(20, 22, 20, 0.62);
    --stage: #d9d9d9;
  }
  * { margin: 0; padding: 0; box-sizing: border-box; }
  html, body {
    width: 1000px; height: 1200px; overflow: hidden;
    background: var(--stage);
    font-family: "Jost", "Futura", sans-serif;
  }
  .flyer {
    position: absolute; left: 100px; top: 40px;
    width: 800px; height: 1120px; overflow: hidden;
    background: var(--paper);
  }
  .flyer-shapes { position: absolute; inset: 0; }
  .brand {
    position: absolute; left: 215px; top: 52px;
    display: flex; align-items: center; gap: 22px;
  }
  .brand-dot {
    width: 64px; height: 64px; border-radius: 50%;
    background: var(--brand-green);
  }
  .brand-name {
    color: var(--ink); font-weight: 500; font-size: 34px; line-height: 1.12;
    border-bottom: 2px solid var(--ink); padding-bottom: 6px; width: 260px;
  }
  .established {
    position: absolute; left: 0; right: 0; top: 272px;
    text-align: center; color: var(--ink-light);
    font-weight: 300; font-size: 50px; letter-spacing: 1px;
  }
  .feature { position: absolute; top: 598px; width: 190px; }
  .feature-icon {
    display: block; margin: 0 auto; width: 98px; height: 98px;
  }
  .feature-text {
    margin-top: 4px; min-height: 112px;
    background: var(--panel); border: 2px solid var(--brand-green); border-radius: 8px;
    color: var(--ink-light); font-size: 19px; font-weight: 400; line-height: 1.3;
    text-align: center; display: flex; align-items: center; justify-content: center;
    padding: 10px 8px;
  }
  .feature--export { left: 58px; }
  .feature--delivery { left: 304px; }
  .feature--showroom { left: 555px; }
  .contact {
    position: absolute; left: 0; right: 0; top: 888px;
    text-align: center; color: var(--ink); font-size: 22px; line-height: 1.25;
  }
  .contact-line { display: flex; justify-content: center; align-items: center; gap: 8px; }
  .contact-address { margin-bottom: 18px; }
  .contact-address .contact-line:first-child { gap: 6px; }
  .contact-phone { margin-bottom: 12px; }
  .contact-email { margin-bottom: 14px; }
  .contact svg { width: 18px; height: 18px; flex: none; }
</style>
</head>
<body>
<main class="flyer">
  <svg class="flyer-shapes" viewBox="0 0 800 1120" aria-hidden="false">
    <rect class="warehouse-photo" x="0" y="0" width="800" height="1120" fill="url(#warehouseTone)" role="img" aria-label="Photo of warehouse shelving stacked with product cartons"/>
    <defs>
      <linearGradient id="warehouseTone" x1="0" y1="0" x2="1" y2="1">
        <stop offset="0" stop-color="#3a3530"/>
        <stop offset="0.5" stop-color="#4b3f36"/>
        <stop offset="1" stop-color="#5a4638"/>
      </linearGradient>
    </defs>
    <!-- header bands -->
    <path d="M0,0 H800 V185 Q400,305 0,185 Z" fill="var(--brand-green)"/>
    <path d="M0,0 H800 V70 Q400,388 0,70 Z" fill="var(--paper)"/>
    <path d="M0,0 H800 V62 Q400,384 0,62 Z" fill="var(--brand-red)"/>
    <path d="M0,0 H800 V14 Q400,400 0,14 Z" fill="var(--paper)"/>
    <!-- footer bands -->
    <path d="M0,900 Q400,794 800,900 V1120 H0 Z" fill="var(--brand-green)"/>
    <path d="M0,906 Q400,806 800,906 V1120 H0 Z" fill="var(--paper)"/>
    <path d="M0,912 Q400,810 800,912 V1120 H0 Z" fill="var(--brand-red)"/>
    <path d="M0,985 Q400,761 800,985 V1120 H0 Z" fill="var(--paper)"/>
  </svg>

  <header class="brand">
    <span class="brand-dot"></span>
    <div class="brand-name">Morvellan<br>Wares, Inc.</div>
  </header>

  <h1 class="established">Established 1983</h1>

  <section class="feature feature--export">
    <svg class="feature-icon" viewBox="0 0 100 100">
      <circle cx="50" cy="50" r="46" fill="rgba(15,15,15,0.7)" stroke="var(--brand-green)" stroke-width="3"/>
      <g fill="none" stroke="#fff" stroke-width="2.2" stroke-linejoin="round">
        <path d="M28,56 H72 L66,66 H34 Z"/>
        <path d="M36,56 V46 H62 V56"/>
        <path d="M42,46 V38 H54 V46"/>
        <path d="M26,72 q6,-4 12,0 t12,0 t12,0 t12,0"/>
      </g>
    </svg>
    <p class="feature-text">We export to<br>most islands<br>in the Caribbean.</p>
  </section>

  <section class="feature feature--delivery">
    <svg class="feature-icon" viewBox="0 0 100 100">
      <circle cx="50" cy="50" r="46" fill="rgba(15,15,15,0.7)" stroke="var(--brand-green)" stroke-width="3"/>
      <g fill="none" stroke="#fff" stroke-width="2.2" stroke-linejoin="round">
        <path d="M36,36 H60 V62 H36 Z"/>
        <path d="M60,44 H69 L75,52 V62 H60"/>
        <circle cx="44" cy="64" r="4"/>
        <circle cx="67" cy="64" r="4"/>
        <path d="M24,44 H32 M26,50 H32 M28,56 H32"/>
      </g>
    </svg>
    <p class="feature-text">We offer<br>next-day delivery,<br>Monday through<br>Friday, islandwide.</p>
  </section>

  <section class="feature feature--showroom">
    <svg class="feature-icon" viewBox="0 0 100 100">
      <circle cx="50" cy="50" r="46" fill="rgba(15,15,15,0.7)" stroke="var(--brand-green)" stroke-width="3"/>
      <g fill="none" stroke="#fff" stroke-width="2.2" stroke-linecap="round">
        <path d="M36,52 V48 a14,14 0 0 1 28,0 V52"/>
        <rect x="32" y="50" width="7" height="12" rx="2"/>
        <rect x="61" y="50" width="7" height="12" rx="2"/>
        <path d="M64,62 q0,8 -10,8 H50"/>
        <path d="M34,74 H66"/>
      </g>
    </svg>
    <p class="feature-text">Clients are always<br>welcomed to visit<br>our showroom,</p>
  </section>

  <footer class="contact">
    <address class="contact-address" style="font-style:normal">
      <div class="contact-line">
        <svg viewBox="0 0 20 20"><path d="M10,1 a6,6 0 0 1 6,6 c0,5 -6,11 -6,11 s-6,-6 -6,-11 a6,6 0 0 1 6,-6 Z" fill="none" stroke="var(--brand-red)" stroke-width="2"/><circle cx="10" cy="7" r="2" fill="var(--brand-red)"/></svg>
        <span>Calle Ledanto #42</span>
      </div>
      <div class="contact-line">Rpto Ind Ledanto</div>
      <div class="contact-line">Bayamón, PR 00958</div>
    </address>
    <div class="contact-line contact-phone">
      <svg viewBox="0 0 20 20"><circle cx="10" cy="10" r="8.5" fill="none" stroke="var(--brand-red)" stroke-width="1.6"/><path d="M7,5.5 l1.8,2.5 -1,1.2 c0.8,1.6 1.6,2.4 3,3 l1.2,-1 2.5,1.8 -1,1.5 c-3.5,0 -7,-3.5 -7,-7 Z" fill="var(--brand-red)"/></svg>
      <span>787-614-3927 / 787-652-7193</span>
    </div>
    <div class="contact-line contact-email">
      <svg viewBox="0 0 20 20"><rect x="2" y="5" width="16" height="11" fill="none" stroke="var(--brand-red)" stroke-width="1.6"/><path d="M2,5 L10,11 L18,5" fill="none" stroke="var(--brand-red)" stroke-width="1.6"/></svg>
      <span>info@morvellanwares.com</span>
    </div>
    <div class="contact-line contact-web">
      <svg viewBox="0 0 20 20"><g fill="none" stroke="var(--brand-red)" stroke-width="1.6"><circle cx="10" cy="10" r="8"/><ellipse cx="10" cy="10" rx="3.5" ry="8"/><path d="M2,10 H18"/></g></svg>
      <span>www.morvellanwares.com</span>
    </div>
  </footer>
</main>
</body>
</html>
```